" Com atendimento personalizado e alta qualidade, atendo os clientes com o objetivo de oferecer Prosperidade e Tranquilidade, sendo o melhor corretor de seguros e consultor de negócios. "

```html
<!DOCTYPE html>
<html lang="pt-BR">
<head>
<meta charset="UTF-8">
<title>Serenavita Seguros &amp; Negócios</title>
<link href="https://fonts.googleapis.com/css2?family=Montserrat:wght@500;600;700;800&family=Cormorant+Garamond:wght@500&display=swap" rel="stylesheet">
<style>
  :root {
    --page-bg: #e9ebee;
    --white: #ffffff;
    --teal: #2aaab9;
    --tab-dark: #0f3e4d;
    --photo-top: #6f8a6a;
    --photo-mid: #9fb39a;
    --photo-low: #3d4a55;
    --photo-base: #1f2a33;
  }
  html, body {
    margin: 0;
    width: 1200px;
    height: 1200px;
    overflow: hidden;
    background: var(--page-bg);
  }
  .canvas {
    position: relative;
    width: 1200px;
    height: 1200px;
  }
  .screen {
    position: absolute;
    left: 340px;
    top: 30px;
    width: 520px;
    height: 1140px;
    border-radius: 44px;
    overflow: hidden;
    font-family: "Montserrat", sans-serif;
    color: var(--white);
  }
  .hero-photo {
    position: absolute;
    inset: 0;
    background:
      radial-gradient(ellipse at 55% 62%, rgba(214,178,150,0.55), transparent 45%),
      linear-gradient(180deg, var(--photo-top) 0%, var(--photo-mid) 35%, #7d8c86 55%, var(--photo-low) 78%, var(--photo-base) 100%);
  }
  .status-bar {
    position: absolute;
    top: 22px;
    left: 38px;
    font-size: 17px;
    font-weight: 600;
  }
  .site-header {
    position: absolute;
    top: 185px;
    left: 0;
    width: 100%;
    text-align: center;
  }
  .brand-name {
    font-family: "Cormorant Garamond", serif;
    font-weight: 500;
    font-size: 40px;
    letter-spacing: 2px;
    line-height: 1;
  }
  .brand-tagline {
    margin-top: 6px;
    font-size: 10px;
    font-weight: 500;
    letter-spacing: 2px;
  }
  .menu-toggle {
    position: absolute;
    top: 196px;
    right: 36px;
    width: 32px;
  }
  .side-tabs {
    position: absolute;
    right: 0;
    top: 380px;
    width: 58px;
    height: 590px;
    background: var(--tab-dark);
    border-radius: 10px 0 0 10px;
    display: flex;
    flex-direction: column;
    align-items: center;
    justify-content: space-around;
  }
  .side-tab {
    writing-mode: vertical-rl;
    transform: rotate(180deg);
    font-size: 13px;
    font-weight: 600;
    letter-spacing: 0.5px;
    white-space: nowrap;
  }
  .side-divider {
    width: 30px;
    height: 1px;
    background: rgba(255,255,255,0.4);
  }
  .headline {
    position: absolute;
    left: 48px;
    top: 820px;
    margin: 0;
    font-size: 64px;
    font-weight: 800;
    line-height: 1.15;
    letter-spacing: 1px;
  }
  .actions {
    position: absolute;
    left: 40px;
    right: 40px;
    top: 1028px;
    display: flex;
    gap: 24px;
  }
  .btn {
    flex: 1;
    height: 44px;
    border-radius: 22px;
    display: flex;
    align-items: center;
    justify-content: center;
    font-size: 14px;
    font-weight: 700;
    letter-spacing: 0.5px;
    color: var(--white);
    box-sizing: border-box;
  }
  .btn-primary { background: var(--teal); }
  .btn-outline {
    border: 1.5px solid rgba(255,255,255,0.8);
    justify-content: flex-start;
    padding-left: 6px;
    gap: 60px;
  }
  .play-icon { width: 32px; height: 32px; }
</style>
</head>
<body>
<div class="canvas">
  <main class="screen">
    <div class="hero-photo" role="img" aria-label="Pai e filho sorrindo dentro de um carro"></div>
    <div class="status-bar">5:20</div>
    <header class="site-header">
      <div class="brand-name">SERENAVITA</div>
      <div class="brand-tagline">SEGUROS &amp; NEGÓCIOS</div>
    </header>
    <svg class="menu-toggle" viewBox="0 0 32 24" aria-label="Menu">
      <rect y="2" width="32" height="3" fill="#fff"/>
      <rect y="11" width="32" height="3" fill="#fff"/>
      <rect y="20" width="32" height="3" fill="#fff"/>
    </svg>
    <nav class="side-tabs">
      <span class="side-tab">2ª VIA DO BOLETO</span>
      <span class="side-divider"></span>
      <span class="side-tab">COMUNICAR OCORRÊNCIA</span>
    </nav>
    <h1 class="headline">A MELHOR<br>PROTEÇÃO</h1>
    <div class="actions">
      <div class="btn btn-primary">FAZER SIMULAÇÃO</div>
      <div class="btn btn-outline">
        <svg class="play-icon" viewBox="0 0 32 32" aria-hidden="true">
          <circle cx="16" cy="16" r="15" fill="rgba(255,255,255,0.15)"/>
          <path d="M13 10 L22 16 L13 22 Z" fill="#fff"/>
        </svg>
        <span>ASSISTA</span>
      </div>
    </div>
  </main>
</div>
</body>
</html>
```